business card deign

Logo needs the following on it.
1. attached logo
2. Tagline - "If it keeps a drink cold or the party going...we do it!"
3. Name- Delia Fenwick, Founder and CPO
4. Address - 418 E. Harlow Avenue, Ste 2204, Tampa, FL. 33719
5. Phone - 720.555.0187

```html
<!DOCTYPE html>
<html lang="en">
<head>
<meta charset="utf-8">
<title>Tidemark Business Card</title>
<link rel="stylesheet" href="https://fonts.googleapis.com/css2?family=Arimo:wght@400;700&display=swap">
<style>
  :root {
    --backdrop: #e6e6e4;
    --card: #262626;
    --card-edge: #1c1c1c;
    --ink: #f2f2f2;
    --ink-soft: #d4d4d4;
    --pattern-dark: #1e1e1e;
    --pattern-light: #4a4a4a;
  }
  * { margin: 0; padding: 0; box-sizing: border-box; }
  html, body {
    width: 1200px;
    height: 801px;
    overflow: hidden;
    background: var(--backdrop);
    font-family: "Arimo", Arial, sans-serif;
  }
  .sheet {
    position: relative;
    width: 1200px;
    height: 801px;
    display: flex;
    align-items: center;
    justify-content: center;
    gap: 40px;
  }
  .card {
    position: relative;
    width: 540px;
    height: 309px;
    background: var(--card);
    border: 1px solid var(--card-edge);
    color: var(--ink);
    overflow: hidden;
  }
  /* front */
  .brand {
    position: absolute;
    left: 0;
    right: 0;
    top: 78px;
    text-align: center;
  }
  .brand-mark {
    display: inline-block;
    width: 16px;
    height: 16px;
    border-radius: 50%;
    background: var(--ink);
    vertical-align: middle;
    margin-right: 12px;
  }
  .brand-name {
    display: inline-block;
    vertical-align: middle;
    font-weight: 700;
    font-size: 30px;
    letter-spacing: 12px;
    color: var(--ink);
  }
  .details {
    position: absolute;
    left: 0;
    right: 0;
    top: 170px;
    display: flex;
    justify-content: center;
    align-items: stretch;
    gap: 18px;
  }
  .person {
    text-align: right;
    padding-top: 8px;
  }
  .person-name {
    font-weight: 700;
    font-size: 17px;
    color: var(--ink);
  }
  .person-role {
    font-size: 13px;
    color: var(--ink-soft);
    margin-top: 3px;
  }
  .divider {
    width: 1px;
    background: var(--ink-soft);
  }
  .contact {
    font-size: 12px;
    line-height: 1.45;
    color: var(--ink-soft);
  }
  .contact-phone {
    font-weight: 700;
    font-size: 13px;
    color: var(--ink);
    display: flex;
    align-items: center;
    gap: 5px;
  }
  .contact-phone svg { width: 11px; height: 11px; }
  /* back */
  .pattern {
    position: absolute;
    inset: 0;
    background: linear-gradient(120deg, var(--pattern-dark) 0%, var(--card) 45%, var(--pattern-light) 100%);
  }
  .back-brand {
    position: absolute;
    right: 58px;
    top: 176px;
    font-weight: 700;
    font-size: 15px;
    letter-spacing: 4px;
    color: var(--ink);
  }
</style>
</head>
<body>
<main class="sheet">
  <section class="card card-front">
    <div class="brand">
      <span class="brand-mark"></span><span class="brand-name">TIDEMARK</span>
    </div>
    <div class="details">
      <div class="person">
        <p class="person-name">Delia Fenwick</p>
        <p class="person-role">Founder and CPO</p>
      </div>
      <div class="divider"></div>
      <div class="contact">
        <p class="contact-phone">
          <svg viewBox="0 0 24 24" aria-hidden="true"><path fill="currentColor" d="M6.6 10.8a15.1 15.1 0 0 0 6.6 6.6l2.2-2.2a1 1 0 0 1 1-.25 11.4 11.4 0 0 0 3.6.57 1 1 0 0 1 1 1V20a1 1 0 0 1-1 1A17 17 0 0 1 3 4a1 1 0 0 1 1-1h3.5a1 1 0 0 1 1 1c0 1.25.2 2.45.57 3.57a1 1 0 0 1-.25 1z"/></svg>
          720.555.0187
        </p>
        <p>418 E. Harlow Avenue</p>
        <p>Ste 2204, Tampa, FL. 33719</p>
      </div>
    </div>
  </section>
  <section class="card card-back">
    <div class="pattern" role="img" aria-label="Repeating tone-on-tone pattern of the brand symbol across the card back"></div>
    <p class="back-brand">TIDEMARK</p>
  </section>
</main>
</body>
</html>
```